Kneadwell Bodycare

We are a Massage Therapy business based in Invercargill, New Zealand. We specialise in Sports and deep tissue massage but also provide relaxation and aromatherapy massage. We would like to see designs that use the the logo.
The final design should promote health and fitness.
Updates

Hi I am getting feedback that my business card picture is poor quality. I got this picture from plaza press under massage. So if you google this image a better quality picture should come up,. If not hope to upload a better image by tomorow, thanks.

Target Market(s)

Sports, people with pain and injuries

Industry/Entity Type

Massage

Requirements
Must have
• Logo, muscle body that is used on the business card, also a poster that matches my business card
Nice to have
• Picture of muscle man, shown on my business card
Should not have
• Not a picture of a real person

```html
<!DOCTYPE html>
<html lang="en">
<head>
<meta charset="utf-8">
<title>Kneadwell Bodycare – Poster</title>
<link rel="stylesheet" href="https://fonts.googleapis.com/css2?family=League+Gothic&family=Oswald:wght@400;500&display=swap">
<style>
  :root {
    --navy: #2b2c6e;
    --sky: #6a9fd8;
    --paper: #ffffff;
    --muscle-light: #e4e4e4;
    --muscle-dark: #8d8d8d;
  }
  html, body {
    margin: 0;
    padding: 0;
    overflow: hidden;
    background: var(--paper);
  }
  .poster {
    position: relative;
    width: 877px;
    height: 1200px;
    overflow: hidden;
    background: var(--paper);
    font-family: "Oswald", sans-serif;
    color: var(--navy);
  }
  .poster-frame {
    position: absolute;
    left: 48px;
    top: 46px;
    width: 787px;
    height: 1114px;
    box-sizing: border-box;
    border: 8px solid var(--navy);
  }
  .anatomy-art {
    position: absolute;
    left: 93px;
    top: 79px;
    width: 211px;
    height: 318px;
    background: linear-gradient(135deg, var(--muscle-light) 0%, var(--muscle-dark) 60%, var(--muscle-light) 100%);
  }
  .headline {
    position: absolute;
    margin: 0;
    font-family: "League Gothic", sans-serif;
    font-weight: 400;
    line-height: 1;
    text-transform: uppercase;
    white-space: nowrap;
  }
  .headline-question {
    left: 308px;
    top: 76px;
    font-size: 134px;
    color: var(--navy);
  }
  .headline-pain {
    left: 455px;
    top: 186px;
    font-size: 186px;
    color: var(--sky);
  }
  .ribbon {
    position: absolute;
    left: 0;
    top: 0;
    width: 877px;
    height: 1200px;
  }
  .ribbon-title {
    position: absolute;
    left: 110px;
    width: 660px;
    top: 409px;
    margin: 0;
    text-align: center;
    white-space: nowrap;
    font-family: "League Gothic", sans-serif;
    font-weight: 400;
    font-size: 92px;
    line-height: 118px;
    color: var(--paper);
  }
  .services {
    position: absolute;
    left: 95px;
    width: 340px;
    top: 566px;
    margin: 0;
    padding: 0;
    list-style: none;
    text-align: center;
  }
  .services li {
    font-weight: 400;
    font-size: 40px;
    line-height: 63px;
    color: var(--navy);
  }
  .prices {
    position: absolute;
    left: 550px;
    top: 688px;
    margin: 0;
  }
  .prices-title {
    margin: 0;
    font-weight: 400;
    font-size: 32px;
    line-height: 44px;
    color: var(--sky);
  }
  .prices-list {
    margin: 0;
    padding: 0;
    list-style: none;
  }
  .prices-list li {
    font-weight: 500;
    font-size: 32px;
    line-height: 44.5px;
    color: var(--navy);
  }
  .brand {
    position: absolute;
    left: 0;
    width: 877px;
    top: 936px;
    display: flex;
    justify-content: center;
    align-items: center;
    gap: 16px;
  }
  .brand-name {
    font-weight: 400;
    font-size: 32px;
    line-height: 1;
    color: var(--navy);
  }
  .brand-dot {
    width: 34px;
    height: 34px;
    border-radius: 50%;
    background: var(--sky);
  }
  .contact {
    position: absolute;
    left: 0;
    width: 877px;
    margin: 0;
    text-align: center;
    line-height: 1;
    white-space: nowrap;
  }
  .contact-therapist {
    top: 1016px;
    font-size: 26px;
    font-weight: 400;
    color: var(--navy);
  }
  .contact-location {
    top: 1062px;
    font-size: 23px;
    font-weight: 400;
    color: var(--sky);
  }
  .contact-location .divider {
    margin: 0 22px;
  }
  .contact-booking {
    top: 1100px;
    font-size: 24px;
    font-weight: 500;
    color: var(--navy);
    display: flex;
    justify-content: center;
    align-items: center;
    gap: 10px;
  }
  .social-square {
    width: 30px;
    height: 30px;
    background: var(--sky);
  }
</style>
</head>
<body>
<main class="poster">
  <div class="poster-frame"></div>

  <div class="anatomy-art" role="img" aria-label="Anatomical illustration of back, shoulder and arm muscles with highlighted pain points"></div>

  <h1 class="headline headline-question">Are you in</h1>
  <p class="headline headline-pain">Pain?</p>

  <svg class="ribbon" viewBox="0 0 877 1200" aria-hidden="true">
    <polygon points="73,409 806,409 770,468 806,527 73,527 110,468" fill="var(--navy)"/>
  </svg>
  <h2 class="ribbon-title">KNEADWELL BODYCARE</h2>

  <ul class="services">
    <li>Deep Tissue</li>
    <li>Sports Massage</li>
    <li>Remedial Massage</li>
    <li>Relaxation</li>
    <li>Aromatherapy</li>
  </ul>

  <section class="prices">
    <h3 class="prices-title">PRICES</h3>
    <ul class="prices-list">
      <li>30 minutes: $40</li>
      <li>60 minutes: $60</li>
      <li>90 minutes: $80</li>
    </ul>
  </section>

  <div class="brand">
    <span class="brand-name">Kneadwell Bodycare</span>
    <span class="brand-dot"></span>
  </div>

  <p class="contact contact-therapist">MARA QUINLAN, BACHELOR OF THERAPEUTIC &amp; SPORTS MASSAGE</p>
  <p class="contact contact-location">18 Harlow St, Invercargill<span class="divider">|</span>www.kneadwell.co.nz</p>
  <p class="contact contact-booking">Book today 0275550182 <span class="social-square"></span> Like us on Friendlink!</p>
</main>
</body>
</html>
```